Doctor in Veterinary Medecine/ veterinarian

I am a vet and would like a buisness card which is simple yet elegant and professional.
My aim is to help as much animals as I can. My main field of expertise are dogs and cats. I would like the card to reflect a "family doctor" feeling.
It should not be the traditional picture of a paw or a dog but yet it should have a sign of a pet on it. I would like to have my name Lina Haddour as well as my profession D.V.M and my number.

Target Market(s)

Lebanese population who have pets

Industry/Entity Type

Doctor

Contact Information for Business Card

Should contain my profession " D.V.M", my full name "Lina Haddour" and my number "0096171552934"

Requirements
Must have
• A certain picture depicting my profession
Nice to have
• Some sort of picture related to pets and animals
Should not have
• A picture of a paw or a dog. I need something more creative

```html
<!DOCTYPE html>
<html lang="en">
<head>
<meta charset="utf-8">
<title>Lina Haddour D.V.M – Business Card</title>
<link rel="stylesheet" href="https://fonts.googleapis.com/css2?family=Cinzel:wght@400&family=Open+Sans:wght@400&display=swap">
<style>
  :root {
    --backdrop: #e9e6e1;
    --card-white: #ffffff;
    --stripe-blue: #0a9fd6;
    --band-purple: #843373;
    --text-light: #f6eef4;
  }
  * { margin: 0; padding: 0; box-sizing: border-box; }
  html, body {
    width: 1200px;
    height: 870px;
    overflow: hidden;
    background: var(--backdrop);
  }
  .canvas {
    width: 1200px;
    height: 870px;
    display: flex;
    align-items: center;
    justify-content: center;
  }
  .business-card {
    width: 480px;
    height: 770px;
    background: var(--card-white);
    display: flex;
    flex-direction: column;
    box-shadow: 0 6px 20px rgba(0, 0, 0, 0.15);
  }
  .card-top {
    height: 440px;
    display: flex;
    flex-direction: column;
    align-items: center;
    justify-content: center;
    gap: 28px;
  }
  .brand-square {
    width: 120px;
    height: 120px;
    background: var(--band-purple);
  }
  .brand-name {
    font-family: "Cinzel", serif;
    font-weight: 400;
    font-size: 34px;
    letter-spacing: 1px;
    color: var(--band-purple);
    line-height: 1;
  }
  .accent-stripe {
    height: 16px;
    background: var(--stripe-blue);
  }
  .card-band {
    flex: 1;
    background: var(--band-purple);
    display: flex;
    flex-direction: column;
    align-items: center;
    padding-top: 96px;
    color: var(--text-light);
  }
  .doctor-name {
    font-family: "Cinzel", serif;
    font-weight: 400;
    font-size: 38px;
    letter-spacing: 1px;
    line-height: 1;
  }
  .doctor-title {
    font-family: "Open Sans", sans-serif;
    font-size: 22px;
    letter-spacing: 2px;
    margin-top: 6px;
  }
  .doctor-phone {
    font-family: "Open Sans", sans-serif;
    font-size: 27px;
    letter-spacing: 1px;
    margin-top: 36px;
  }
</style>
</head>
<body>
  <main class="canvas">
    <article class="business-card">
      <section class="card-top">
        <div class="brand-square"></div>
        <p class="brand-name">Lina Haddour</p>
      </section>
      <div class="accent-stripe"></div>
      <section class="card-band">
        <h1 class="doctor-name">Dr.Lina Haddour</h1>
        <p class="doctor-title">D.V.M</p>
        <p class="doctor-phone">0096171552934</p>
      </section>
    </article>
  </main>
</body>
</html>
```